Velmora Tidewalk - Needs image for website and marketing materials

Velmora Tidewalk needs a graphic design to visually communicate their cloud based fertility organizer app. We would like to see bright colors used that work well with the pink in our logo. The design should communicate that a complex process is easier to manage with our app.

You can get more details about our app at www.velmoratidewalk.com

Target Market(s)

Women that are pursuing a family (20 something - 40 something)

Industry/Entity Type

Graphic Design

Requirements
Must have
• The design should include an Lumaro image to communicate our app can be used by smartphones. This image may be used on website, posters and other marketing materials.
I have added 3 files to the project. Use the general png image for the Lumaro app screen and not the one with the phone image with the screen shot.
Nice to have
• I would like to connect the colors already used for each of the categories within the app to maybe icons that represent these categories (appointment, medication, lab test, procedures, natural) like is displayed in the sample images attached.

```html
<!DOCTYPE html>
<html lang="en">
<head>
<meta charset="utf-8">
<title>Velmora Tidewalk – Fertility Organizer App</title>
<link href="https://fonts.googleapis.com/css2?family=Arimo:wght@400;700&display=swap" rel="stylesheet">
<style>
  :root{
    --bg:#ffffff;
    --phone-body:#f4f4f6;
    --phone-edge:#c9cacf;
    --bezel:#1c1c1f;
    --screen:#e9ebee;
    --status:#d7dbe1;
    --toolbar:#c5cad2;
    --brand-pink:#ec3d78;
    --appointment:#b9a2d2;
    --medication:#f3ee86;
    --labtest:#e38f8f;
    --procedure:#8fd2df;
    --natural:#c2e29c;
    --ink:#1d1d1d;
    --muted:#6d7178;
  }
  *{box-sizing:border-box;margin:0;padding:0}
  html,body{width:1200px;height:638px;overflow:hidden;background:var(--bg)}
  body{font-family:"Arimo",Arial,sans-serif;position:relative}

  .app-icon{position:absolute;border-radius:22%;box-shadow:0 6px 12px rgba(0,0,0,.25)}
  .icon-blue{background:linear-gradient(150deg,#8fe4ff,#1aa3e6)}
  .icon-yellow{background:linear-gradient(150deg,#fff47a,#f2c21a)}
  .icon-green{background:linear-gradient(150deg,#b6f04a,#3a9a12)}
  .icon-orange{background:linear-gradient(150deg,#ffb24a,#f0461a)}
  .icon-peach{background:linear-gradient(150deg,#ffe0a0,#f59032)}
  .icon-purple{background:linear-gradient(150deg,#e59bff,#9a2fd8)}
  .icon-red{background:linear-gradient(150deg,#ff8a7a,#e02222)}
  .icon-pink{background:linear-gradient(150deg,#ffa3d8,#e43ca0)}
  .icon-teal{background:linear-gradient(150deg,#8ff5e0,#1ab8a0)}
  .icon-lime{background:linear-gradient(150deg,#f0ff8a,#a8d41a)}

  .phone{position:absolute;left:433px;top:-6px;width:340px;height:628px;border-radius:52px;
    background:var(--phone-body);border:3px solid var(--phone-edge);box-shadow:0 4px 14px rgba(0,0,0,.2)}
  .phone-speaker{position:absolute;left:136px;top:68px;width:62px;height:8px;border-radius:4px;background:#9ea2a8}
  .phone-home{position:absolute;left:136px;top:550px;width:64px;height:64px;border-radius:50%;border:3px solid #cfd1d5;background:#fafafa}
  .screen{position:absolute;left:30px;top:128px;width:274px;height:392px;background:var(--screen);border:2px solid var(--bezel);overflow:hidden}
  .status-bar{height:14px;background:var(--status);display:flex;justify-content:space-between;align-items:center;padding:0 6px;font-size:10px;font-weight:700;color:var(--ink)}
  .browser-bar{background:#c3cad3;padding:3px 6px 6px}
  .browser-title{text-align:center;font-size:10px;color:#333}
  .browser-fields{display:flex;gap:6px;margin-top:3px}
  .url-field{flex:1;height:22px;border-radius:5px;background:#fff;font-size:11px;line-height:22px;padding:0 6px;color:#333;white-space:nowrap;overflow:hidden}
  .search-field{width:76px;height:22px;border-radius:11px;background:#fff;font-size:10px;line-height:22px;padding-left:9px;color:#999}
  .app-header{height:34px;background:var(--brand-pink);display:flex;align-items:center;position:relative}
  .back-button{margin-left:6px;font-size:10px;color:#fff;border:1.5px solid #fff;border-radius:5px;padding:3px 7px}
  .app-title{position:absolute;left:0;right:0;text-align:center;font-size:17px;font-weight:700;color:#fff}
  .event-label{font-size:13px;font-weight:700;color:var(--muted);padding:10px 10px 6px}
  .event-type{margin:0 8px 5px;height:34px;border-radius:4px;font-size:13px;font-weight:700;color:var(--ink);padding-left:8px;line-height:34px}
  .type-appointment{background:var(--appointment)}
  .type-medication{background:var(--medication)}
  .type-labtest{background:var(--labtest)}
  .type-procedure{background:var(--procedure)}
  .type-natural{background:var(--natural)}
  .toolbar{position:absolute;left:0;right:0;bottom:0;height:32px;background:var(--toolbar)}
</style>
</head>
<body>

<!-- scattered small icons, left cluster -->
<div class="app-icon icon-pink"   style="left:385px;top:60px;width:30px;height:30px;transform:rotate(12deg)" role="img" aria-label="Small app icon"></div>
<div class="app-icon icon-purple" style="left:320px;top:118px;width:46px;height:46px;transform:rotate(-14deg)" role="img" aria-label="Health app icon"></div>
<div class="app-icon icon-teal"   style="left:265px;top:92px;width:28px;height:28px;transform:rotate(20deg)" role="img" aria-label="Small app icon"></div>
<div class="app-icon icon-red"    style="left:168px;top:232px;width:64px;height:64px;transform:rotate(-12deg)" role="img" aria-label="Heart monitor icon"></div>
<div class="app-icon icon-orange" style="left:246px;top:170px;width:34px;height:34px;transform:rotate(10deg)" role="img" aria-label="Small app icon"></div>
<div class="app-icon icon-lime"   style="left:110px;top:300px;width:30px;height:30px;transform:rotate(-18deg)" role="img" aria-label="Small app icon"></div>
<div class="app-icon icon-blue"   style="left:220px;top:476px;width:54px;height:54px;transform:rotate(16deg)" role="img" aria-label="Notes app icon"></div>
<div class="app-icon icon-pink"   style="left:395px;top:248px;width:34px;height:34px;transform:rotate(-8deg)" role="img" aria-label="Small app icon"></div>
<div class="app-icon icon-yellow" style="left:388px;top:330px;width:30px;height:30px;transform:rotate(14deg)" role="img" aria-label="Small app icon"></div>

<!-- large left icons -->
<div class="app-icon icon-blue"   style="left:228px;top:192px;width:156px;height:170px;transform:rotate(-12deg)" role="img" aria-label="Clipboard appointment icon"></div>
<div class="app-icon icon-yellow" style="left:138px;top:324px;width:142px;height:142px;transform:rotate(-6deg)" role="img" aria-label="Syringe medication icon"></div>
<div class="app-icon icon-green"  style="left:266px;top:378px;width:192px;height:192px;transform:rotate(8deg)" role="img" aria-label="Leaves natural icon"></div>

<!-- right cluster small icons -->
<div class="app-icon icon-yellow" style="left:790px;top:70px;width:30px;height:30px;transform:rotate(-12deg)" role="img" aria-label="Small app icon"></div>
<div class="app-icon icon-green"  style="left:835px;top:120px;width:44px;height:44px;transform:rotate(18deg)" role="img" aria-label="Small app icon"></div>
<div class="app-icon icon-teal"   style="left:900px;top:168px;width:52px;height:52px;transform:rotate(-10deg)" role="img" aria-label="Checklist app icon"></div>
<div class="app-icon icon-pink"   style="left:975px;top:210px;width:34px;height:34px;transform:rotate(14deg)" role="img" aria-label="Small app icon"></div>
<div class="app-icon icon-red"    style="left:1010px;top:290px;width:30px;height:30px;transform:rotate(-16deg)" role="img" aria-label="Small app icon"></div>
<div class="app-icon icon-lime"   style="left:1012px;top:392px;width:52px;height:52px;transform:rotate(18deg)" role="img" aria-label="Small app icon"></div>
<div class="app-icon icon-orange" style="left:950px;top:108px;width:28px;height:28px;transform:rotate(10deg)" role="img" aria-label="Small app icon"></div>
<div class="app-icon icon-blue"   style="left:780px;top:178px;width:30px;height:30px;transform:rotate(-20deg)" role="img" aria-label="Small app icon"></div>

<!-- large right icons -->
<div class="app-icon icon-purple" style="left:915px;top:262px;width:88px;height:88px;transform:rotate(10deg)" role="img" aria-label="Calendar icon"></div>
<div class="app-icon icon-orange" style="left:762px;top:216px;width:138px;height:146px;transform:rotate(8deg)" role="img" aria-label="Syringe procedure icon"></div>
<div class="app-icon icon-peach"  style="left:880px;top:394px;width:134px;height:146px;transform:rotate(-8deg)" role="img" aria-label="Microscope lab test icon"></div>
<div class="app-icon icon-yellow" style="left:700px;top:366px;width:180px;height:196px;transform:rotate(-6deg)" role="img" aria-label="Capsule pill medication icon"></div>

<!-- Lumaro smartphone -->
<div class="phone" aria-label="Lumaro smartphone showing Velmora Tidewalk app">
  <div class="phone-speaker"></div>
  <div class="screen">
    <div class="status-bar"><span>Nexacell</span><span>1:36 PM</span><span>90%</span></div>
    <div class="browser-bar">
      <div class="browser-title">VT Mobile</div>
      <div class="browser-fields">
        <div class="url-field">calendar.velmoratidewalk.com</div>
        <div class="search-field">Searchly</div>
      </div>
    </div>
    <div class="app-header"><span class="back-button">back</span><span class="app-title">Add Event</span></div>
    <div class="event-label">Event Type</div>
    <div class="event-type type-appointment">Appointment</div>
    <div class="event-type type-medication">Medication</div>
    <div class="event-type type-labtest">Lab Test</div>
    <div class="event-type type-procedure">Procedure</div>
    <div class="event-type type-natural">Natural</div>
    <div class="toolbar"></div>
  </div>
  <div class="phone-home"></div>
</div>

</body>
</html>
```